Recruitment technology firm needs a downloadable pdf to generate leads.

We need design work for a downloadable pdf that will serve as an educational document to visitors to our website. We help clients identify candidates that fit their job posting. We do that by defining the personality of the job and then assessing the personality of the candidates. We then mathematically compare and rank all the candidates against the job. Our colour scheme is blue. The final design should move from communicating a lack of fit or frustration to people fitting their job and success per the text we have built. People who download this lead generator will be added to our email list for re-marketing purposes. our website is www.tallowridgeadvisory.com. I've attached an example of a lead generator (ebike)for a business unrelated to ours.

Target Market(s)

Our target market is businesses of 50-300 people, we're targeting business owners or executives of entrepreneurial (vs. corporate) companies.

Colors
85acd3
3377b5
0455a3

Requirements
Must have
• Easy to read so text isn't overwhelming.
Nice to have
• Don't be compelled to use our website photos or those like it. I'd like this to reflect entrepreneurial companies, not corporate, suit and tie companies.

```html
<!DOCTYPE html>
<html lang="en">
<head>
<meta charset="utf-8">
<title>So how can you hire for fit?</title>
<link rel="stylesheet" href="https://fonts.googleapis.com/css2?family=Questrial&family=Montserrat:wght@700&display=swap">
<style>
  :root {
    --page-bg: #e4e1e0;
    --panel: #10546e;
    --panel-shadow: rgba(0, 0, 0, 0.75);
    --title: #3fc3f0;
    --body-text: #ffffff;
    --band-blue: #1e6fa6;
    --label-primary: #0399cc;
    --label-secondary: #86bbdc;
    --grid-line: #8c8c8c;
    --axis-bg: #e9e9e9;
    --job-red: #e8213a;
    --candidate-black: #1b1b1b;
  }
  * { margin: 0; padding: 0; box-sizing: border-box; }
  html, body { width: 848px; height: 1200px; overflow: hidden; }
  body {
    position: relative;
    background: radial-gradient(ellipse at 30% 20%, #efedec 0%, var(--page-bg) 60%, #d9d6d5 100%);
    font-family: "Questrial", "Century Gothic", sans-serif;
  }
  .content-panel {
    position: absolute;
    left: 23px; top: 34px;
    width: 805px; height: 1032px;
    background: var(--panel);
    border-radius: 68px;
    box-shadow: 0 0 14px 4px var(--panel-shadow);
  }
  .page-title {
    position: absolute;
    left: 74px; top: 40px;
    font-weight: 400;
    font-size: 45px;
    letter-spacing: -1.2px;
    color: var(--title);
    white-space: nowrap;
  }
  .copy {
    position: absolute;
    left: 48px;
    color: var(--body-text);
    font-size: 23px;
    line-height: 29px;
    letter-spacing: -0.6px;
    white-space: nowrap;
  }
  .copy-intro { top: 114px; }
  .copy-benchmark { top: 226px; }
  .copy-survey { top: 454px; line-height: 28.5px; }
  .copy-insight { top: 576px; line-height: 25px; }
  .copy-outcome { top: 638px; left: 52px; }
  .copy-chart-intro { top: 689px; line-height: 25px; }
  .fit-chart {
    position: absolute;
    left: 107px; top: 752px;
    width: 639px; height: 290px;
  }
  .fit-chart .row-label {
    font-family: "Montserrat", "Arial", sans-serif;
    font-weight: 700;
    font-size: 15px;
    fill: #ffffff;
  }
  .fit-chart .tick-label {
    font-family: "Montserrat", "Arial", sans-serif;
    font-weight: 700;
    font-size: 16px;
    fill: #555555;
  }
  .bottom-swoosh {
    position: absolute;
    left: 0; bottom: 0;
    width: 848px; height: 140px;
  }
</style>
</head>
<body>

  <div class="content-panel"></div>

  <h1 class="page-title">So how can you hire for fit?</h1>

  <p class="copy copy-intro">Personality is the most significant predictor of both fit to the manager and<br>&nbsp;performance in the role.. It is also one of the most difficult things to assess<br>without the use of an objective tool.</p>

  <p class="copy copy-benchmark">&nbsp;Most candidates behave a certain way in an interview,but it may be<br>that is difficult for them to sustain.To start addressing the problem of<br>hiring bad fits you need to add more objectivity to your process.<br>&nbsp;FitLens is a tool designed to define a benchmark of what personality<br>&nbsp;is required in a role using data. Everyone gets on the same page of what<br>&nbsp;success looks like.</p>

  <p class="copy copy-survey">&nbsp;From there each candidate completes a TraitScan personality survey within<br>within the FitLens tool. Then they are compared equally to the<br>benchmark and ranked objectively. All candidates are compared using the<br>&nbsp;same personality dimensions.</p>

  <p class="copy copy-insight">You leverage specific data and our insight to find the best candidates …<br>&nbsp;Your ability to consistently hire above average fits increases</p>

  <p class="copy copy-outcome">You achieve more.</p>

  <p class="copy copy-chart-intro">Here are the results of a candidate compared to a job. The job is<br>represented in red, the candidate is represented in black.</p>

  <svg class="fit-chart" viewBox="0 0 1223 555" role="img" aria-label="Chart comparing job benchmark in red with candidate results in black across seven personality dimensions">
    <rect x="0" y="0" width="1223" height="555" fill="#ffffff"/>
    <rect x="4" y="7" width="1214" height="544" fill="none" stroke="var(--grid-line)" stroke-width="3"/>

    <!-- axis bands -->
    <rect x="5" y="270" width="1212" height="40" fill="var(--axis-bg)"/>
    <rect x="5" y="508" width="1212" height="43" fill="var(--axis-bg)"/>

    <!-- label cells -->
    <g fill="var(--label-primary)">
      <rect x="5" y="8" width="188" height="64"/>
      <rect x="5" y="74" width="188" height="64"/>
      <rect x="5" y="140" width="188" height="64"/>
      <rect x="5" y="206" width="188" height="63"/>
    </g>
    <g fill="var(--label-secondary)">
      <rect x="5" y="311" width="188" height="65"/>
      <rect x="5" y="377" width="188" height="65"/>
      <rect x="5" y="443" width="188" height="64"/>
    </g>

    <!-- row dividers -->
    <g stroke="var(--grid-line)" stroke-width="2.5">
      <line x1="5" y1="73" x2="1217" y2="73"/>
      <line x1="5" y1="139" x2="1217" y2="139"/>
      <line x1="5" y1="205" x2="1217" y2="205"/>
      <line x1="5" y1="269" x2="1217" y2="269"/>
      <line x1="5" y1="310" x2="1217" y2="310"/>
      <line x1="5" y1="376" x2="1217" y2="376"/>
      <line x1="5" y1="442" x2="1217" y2="442"/>
      <line x1="5" y1="507" x2="1217" y2="507"/>
    </g>

    <text class="row-label" x="18" y="46">ASSERTIVENESS</text>
    <text class="row-label" x="18" y="114">SOCIABILITY</text>
    <text class="row-label" x="18" y="179">PACE</text>
    <text class="row-label" x="18" y="232">DETAIL</text>
    <text class="row-label" x="18" y="253">ORIENTATION</text>
    <text class="row-label" x="18" y="338">BEHAVIORAL</text>
    <text class="row-label" x="18" y="359">ADAPTABILITY</text>
    <text class="row-label" x="18" y="416">EMOTIVENESS</text>
    <text class="row-label" x="18" y="481">CREATIVITY</text>

    <!-- top axis ticks -->
    <g stroke="#777" stroke-width="2">
      <line x1="237" y1="270" x2="237" y2="277"/><line x1="330" y1="270" x2="330" y2="277"/>
      <line x1="424" y1="270" x2="424" y2="277"/><line x1="517" y1="270" x2="517" y2="277"/>
      <line x1="610" y1="270" x2="610" y2="277"/><line x1="704" y1="270" x2="704" y2="277"/>
      <line x1="797" y1="270" x2="797" y2="277"/><line x1="890" y1="270" x2="890" y2="277"/>
      <line x1="983" y1="270" x2="983" y2="277"/><line x1="1077" y1="270" x2="1077" y2="277"/>
      <line x1="1170" y1="270" x2="1170" y2="277"/>
    </g>
    <g class="tick-label" text-anchor="middle">
      <text x="237" y="298">-5</text><text x="330" y="298">-4</text><text x="424" y="298">-3</text>
      <text x="517" y="298">-2</text><text x="610" y="298">-1</text><text x="704" y="298">0</text>
      <text x="797" y="298">1</text><text x="890" y="298">2</text><text x="983" y="298">3</text>
      <text x="1077" y="298">4</text><text x="1170" y="298">5</text>
    </g>

    <!-- bottom axis ticks -->
    <g stroke="#777" stroke-width="2">
      <line x1="240" y1="508" x2="240" y2="515"/><line x1="333" y1="508" x2="333" y2="515"/>
      <line x1="426" y1="508" x2="426" y2="515"/><line x1="519" y1="508" x2="519" y2="515"/>
      <line x1="612" y1="508" x2="612" y2="515"/><line x1="705" y1="508" x2="705" y2="515"/>
      <line x1="798" y1="508" x2="798" y2="515"/><line x1="891" y1="508" x2="891" y2="515"/>
      <line x1="984" y1="508" x2="984" y2="515"/><line x1="1077" y1="508" x2="1077" y2="515"/>
      <line x1="1170" y1="508" x2="1170" y2="515"/>
    </g>
    <g class="tick-label" text-anchor="middle">
      <text x="240" y="538">0</text><text x="333" y="538">1</text><text x="426" y="538">2</text>
      <text x="519" y="538">3</text><text x="612" y="538">4</text><text x="705" y="538">5</text>
      <text x="798" y="538">6</text><text x="891" y="538">7</text><text x="984" y="538">8</text>
      <text x="1077" y="538">9</text><text x="1170" y="538">10</text>
    </g>

    <!-- zero reference -->
    <line x1="704" y1="8" x2="704" y2="268" stroke="#9a9a9a" stroke-width="2" stroke-dasharray="7 6"/>

    <!-- job benchmark -->
    <polyline points="850,30 792,102 517,167 669,234" fill="none" stroke="var(--job-red)" stroke-width="3" stroke-dasharray="6 5"/>
    <g fill="var(--job-red)">
      <rect x="841" y="21" width="18" height="18"/>
      <rect x="783" y="93" width="18" height="18"/>
      <rect x="508" y="158" width="18" height="18"/>
      <rect x="660" y="225" width="18" height="18"/>
      <rect x="792" y="336" width="18" height="18"/>
      <rect x="792" y="404" width="18" height="18"/>
      <rect x="792" y="467" width="18" height="18"/>
    </g>

    <!-- candidate -->
    <polyline points="877,30 660,93 612,167 696,234" fill="none" stroke="var(--candidate-black)" stroke-width="3"/>
    <g fill="var(--candidate-black)">
      <circle cx="877" cy="30" r="9"/>
      <circle cx="660" cy="93" r="9"/>
      <circle cx="612" cy="167" r="9"/>
      <circle cx="696" cy="234" r="9"/>
      <circle cx="954" cy="345" r="9"/>
      <circle cx="1083" cy="413" r="9"/>
      <circle cx="832" cy="476" r="9"/>
    </g>
  </svg>

  <svg class="bottom-swoosh" viewBox="0 0 848 140" preserveAspectRatio="none" aria-hidden="true">
    <defs>
      <linearGradient id="swoosh-fill" x1="0" y1="0" x2="0" y2="1">
        <stop offset="0" stop-color="#cfcfcf"/>
        <stop offset="0.5" stop-color="#f4f4f4"/>
        <stop offset="1" stop-color="#ffffff"/>
      </linearGradient>
    </defs>
    <path d="M0 108 C 200 60, 420 12, 560 10 C 680 8, 780 30, 848 48 L 848 140 L 0 140 Z" fill="var(--band-blue)"/>
    <path d="M0 118 C 200 70, 420 20, 560 18 C 680 16, 780 38, 848 56 L 848 140 L 0 140 Z" fill="url(#swoosh-fill)"/>
  </svg>

</body>
</html>
```